Summer Fun

I need a Poster for Front of hotel advertising discounted drinks on Thursday & Fridays
$3.50.
Schooners of Local Beer, Glass of House Wine & Bubbly.
From 3.30pm to 6.30 pm
Nibblies Provided

25 + Market

Hotel

• Do not want to be known as Happy Hour.

```html
<!DOCTYPE html>
<html lang="en">
<head>
<meta charset="utf-8">
<title>Thursday &amp; Friday Drinks Poster</title>
<link rel="stylesheet" href="https://fonts.googleapis.com/css2?family=Anton&family=Oswald:wght@400;500&family=Roboto+Condensed:wght@700&display=swap">
<style>
  :root {
    --green-light: #d3ea8f;
    --green-mid: #a8cf4a;
    --green-deep: #7fb22a;
    --ink: #1a1714;
    --white: #ffffff;
    --foam: #f7f6f0;
    --beer-light: #f2c75a;
    --beer-deep: #c98a16;
  }
  html, body {
    margin: 0;
    padding: 0;
    overflow: hidden;
  }
  .poster {
    position: relative;
    width: 846px;
    height: 1200px;
    overflow: hidden;
    background:
      radial-gradient(ellipse at 65% 45%, var(--green-light) 0%, var(--green-mid) 55%, var(--green-deep) 100%);
    color: var(--ink);
  }
  .beer-photo {
    position: absolute;
    left: 58px;
    top: 218px;
    width: 292px;
    height: 960px;
    border-radius: 40% 40% 18% 18% / 10% 10% 6% 6%;
    background: linear-gradient(to bottom,
      var(--foam) 0%, var(--foam) 30%,
      var(--beer-light) 36%, var(--beer-deep) 75%,
      #e9e3cc 90%, #cfd6c0 100%);
    opacity: 0.92;
  }
  .headline {
    position: absolute;
    left: 48px;
    top: 36px;
    width: 760px;
    margin: 0;
    font-family: "Oswald", sans-serif;
    font-weight: 400;
    font-size: 136px;
    line-height: 1;
    letter-spacing: -3px;
    white-space: nowrap;
    transform: scaleX(0.86);
    transform-origin: left top;
  }
  .headline .amp { color: var(--white); }
  .price {
    position: absolute;
    right: 46px;
    top: 222px;
    margin: 0;
    font-family: "Anton", sans-serif;
    font-size: 190px;
    line-height: 1;
    letter-spacing: -2px;
  }
  .hours {
    position: absolute;
    right: 46px;
    top: 402px;
    margin: 0;
    font-family: "Roboto Condensed", sans-serif;
    font-weight: 700;
    font-size: 46px;
    line-height: 1;
  }
  .offer-list {
    position: absolute;
    left: 419px;
    top: 483px;
    width: 399px;
    margin: 0;
    padding: 0;
    list-style: none;
    border-top: 3px solid var(--ink);
  }
  .offer-item {
    border-bottom: 3px solid var(--ink);
    padding: 12px 18px 6px 0;
    text-align: right;
    font-family: "Anton", sans-serif;
    font-size: 78px;
    line-height: 73px;
    text-transform: uppercase;
  }
  .offer-item.bubbly { padding-bottom: 16px; }
  .nibblies {
    position: absolute;
    right: 46px;
    top: 1118px;
    margin: 0;
    font-family: "Oswald", sans-serif;
    font-weight: 500;
    font-size: 56px;
    line-height: 1;
    transform: scaleX(0.82);
    transform-origin: right top;
    white-space: nowrap;
  }
</style>
</head>
<body>
  <main class="poster">
    <div class="beer-photo" role="img" aria-label="Photo of a tall glass of cold golden beer with a frothy white head"></div>

    <h1 class="headline">THURSDAY<span class="amp">&amp;</span>FRIDAY</h1>
    <p class="price">$3.50</p>
    <p class="hours">3:30pm - 6:30pm</p>

    <ul class="offer-list">
      <li class="offer-item">Schooners<br>of local<br>beer</li>
      <li class="offer-item">Glass<br>of house<br>wine</li>
      <li class="offer-item bubbly">Bubbly</li>
    </ul>

    <p class="nibblies">NIBBLIES PROVIDED</p>
  </main>
</body>
</html>
```